Business card for marketing analytics company

Need a business card for new company. I have a logo already that I want to be built into the card and should use those colours

Company is called steered by tallies
Design must bring steered by tallies to life not be a card that could be for anyone with a logo put on it.

Like the front to be fairly clean and uncluttered bringing the logo out with a suitable design on the back of the card.

The logo represents a compass and business growth so those themes along with numbers, analytics , data are appropriate.
I'm often working with creative industries so also needs to reflect the creative side of analytics rather than be very corporate looking.

Target Market(s)

Ad agency, media agency, consumer goods clients

Industry/Entity Type

Market Research

Contact Information for Business Card

Needs to include name, title, email and phone number

Colors
f78f20
f68d4d
ec1f27

Requirements
Must have
• Must bring steered by tallies to life not be a card that could be for anyone with a logo put on it.
• Logo, Correct colours
• Like a design on the back that relates to company name
• Designs for both sides
Should not have
• Please do not just submit logo and a coloured card.
• It needs to have a design element to it
• No black background
• No clear cards - needs front & back

```html
<!DOCTYPE html>
<html lang="en">
<head>
<meta charset="utf-8">
<title>Larkspur Metrics — Business Card</title>
<link rel="stylesheet" href="https://fonts.googleapis.com/css2?family=Open+Sans:wght@400;600;700&display=swap">
<style>
  :root {
    --page-bg: #e6e6e8;
    --brand-red: #ec1f27;
    --brand-red-deep: #b3161d;
    --brand-orange: #f78f20;
    --brand-orange-soft: #f68d4d;
    --brand-orange-deep: #e8661f;
    --ink-grey: #5b6770;
    --paper: #ffffff;
    --white: #ffffff;
  }
  * { box-sizing: border-box; margin: 0; padding: 0; }
  html, body {
    width: 1200px; height: 843px; overflow: hidden;
    background: var(--page-bg);
    font-family: "Open Sans", Arial, sans-serif;
  }
  .stage {
    position: relative; width: 1200px; height: 843px;
    display: flex; align-items: center; justify-content: center; gap: 40px;
  }
  .card {
    position: relative; width: 540px; height: 309px; overflow: hidden;
    box-shadow: 0 10px 28px rgba(0,0,0,.18);
  }

  /* Back side */
  .card--back {
    background: linear-gradient(135deg, var(--brand-red) 0%, #d01c23 55%, var(--brand-red-deep) 100%);
    color: var(--white);
  }
  .card--back .wordmark {
    position: absolute; left: 0; right: 0; top: 114px;
    display: flex; align-items: center; justify-content: center; gap: 16px;
  }
  .card--back .wordmark__dot {
    width: 54px; height: 54px; border-radius: 50%;
    border: 2px solid var(--white);
  }
  .card--back .wordmark__name {
    font-weight: 600; font-size: 28px; line-height: 1; color: var(--white);
  }
  .card--back .web {
    position: absolute; left: 0; right: 0; top: 212px; text-align: center;
    font-size: 11px; letter-spacing: 6px; color: var(--white);
  }

  /* Front side */
  .card--front { background: var(--paper); }
  .card--front .wordmark {
    position: absolute; left: 36px; top: 56px;
    display: flex; align-items: center; gap: 14px;
  }
  .card--front .wordmark__dot {
    width: 48px; height: 48px; border-radius: 50%;
    background: var(--brand-orange);
  }
  .card--front .wordmark__name {
    font-weight: 600; font-size: 26px; line-height: 1; color: var(--ink-grey);
  }
  .wave { position: absolute; left: 0; top: 0; width: 540px; height: 309px; }
  .contact {
    position: absolute; right: 22px; bottom: 18px; text-align: right; color: var(--white);
  }
  .contact__name { font-weight: 700; font-size: 16px; line-height: 1.1; }
  .contact__title { font-size: 13px; margin-bottom: 8px; }
  .contact__line {
    display: flex; align-items: center; justify-content: flex-end; gap: 6px;
    font-size: 12px; line-height: 19px;
  }
  .contact__icon { width: 12px; height: 12px; flex: none; }
</style>
</head>
<body>
<main class="stage">

  <section class="card card--back" aria-label="Card back">
    <div class="wordmark">
      <span class="wordmark__dot"></span>
      <span class="wordmark__name">Larkspur Metrics</span>
    </div>
    <p class="web">www.larkspurmetrics.com</p>
  </section>

  <section class="card card--front" aria-label="Card front">
    <div class="wordmark">
      <span class="wordmark__dot"></span>
      <span class="wordmark__name">Larkspur Metrics</span>
    </div>

    <svg class="wave" viewBox="0 0 540 309" aria-hidden="true">
      <defs>
        <linearGradient id="waveFill" x1="0" y1="0" x2="1" y2="1">
          <stop offset="0" stop-color="#f78f20"/>
          <stop offset="0.6" stop-color="#f68d4d"/>
          <stop offset="1" stop-color="#e8661f"/>
        </linearGradient>
      </defs>
      <path d="M0 196 C 80 225, 150 268, 240 238 C 330 205, 400 150, 470 152 C 505 153, 525 158, 540 162 L540 309 L0 309 Z" fill="url(#waveFill)"/>
      <path d="M0 192 C 80 221, 150 264, 240 234 C 330 201, 400 146, 470 148 C 505 149, 525 154, 540 158" fill="none" stroke="#ec1f27" stroke-width="2"/>
    </svg>

    <div class="contact">
      <p class="contact__name">Mara Lindqvist</p>
      <p class="contact__title">President</p>
      <p class="contact__line">555 0142 7789
        <svg class="contact__icon" viewBox="0 0 12 12" aria-hidden="true"><path d="M2 1h2.5l1 2.5-1.3 1a6 6 0 0 0 3.3 3.3l1-1.3 2.5 1V10a1 1 0 0 1-1 1A9 9 0 0 1 1 2a1 1 0 0 1 1-1z" fill="#fff"/></svg>
      </p>
      <p class="contact__line">mara@larkspurmetrics.com
        <svg class="contact__icon" viewBox="0 0 12 12" aria-hidden="true"><rect x="0.5" y="2" width="11" height="8" fill="#fff"/><path d="M0.5 2 6 6.5 11.5 2" fill="none" stroke="#e8661f" stroke-width="1"/></svg>
      </p>
      <p class="contact__line">www.larkspurmetrics.com
        <svg class="contact__icon" viewBox="0 0 12 12" aria-hidden="true"><circle cx="6" cy="6" r="5.5" fill="#fff"/><path d="M6 2.5v3.5l2.2 1.5" fill="none" stroke="#e8661f" stroke-width="1.2"/></svg>
      </p>
    </div>
  </section>

</main>
</body>
</html>
```